Business cards and Stationary | Corvel Music Events

Hello! We need business cards and stationery for a new small business in the music industry. "Corvel is a high-end music agency which provides an unparalleled level of talent and personalized service to the realm entertainment, corporate events, and luxury weddings. Here is where the classical meets the contemporary and we can bring your vision to life.Keeping a steady finger on the pulse of current trends and consistently raising the bar for industry standards, Corvel continues to rise to the forefront of the music industry, providing the utmost professional, high-end, elegant, and engaging entertainment in Australia and World-Wide."

Target Market(s)

Class A. high profile corporate business.

Industry/Entity Type

Entertainment

Contact Information for Business Card

Corvel Music Events

Tessa Holloway
Director | Violinist

Level 7, 41 Marlow Street
Sydney, 2000

Website: www.corvelmusicevents.com
Phone number: 0481 352 604
Email: tessa@corvelmusicevents.com

Font styles to use
Serif
Sans Serif
Script

Colors
feeeee
0355a3
f59296
ffffff

Requirements
Nice to have
• Clean and sophisticated would be perfect.
• If there is a way to include the Instagram without being tacky, that would be awesome
• @corvelmusicevents
• Our website and logo have the following fonts:
• The primary logo is inspired and based on a font called BillionScript but the B is completely hand drawn and the rest is customised a bit to work together cohesively
• Monserrat Light - Is the Music part of the logo and as headers in the site
• Open Sans 300 and 400 (Light or Regular) is used mostly as the body text in the site
• If you want to access the website:
• www.corvelmusicevents.com
• username: client
• password: preview

```html
<!DOCTYPE html>
<html lang="en">
<head>
<meta charset="utf-8">
<title>Corvel Music Events — Business Cards</title>
<link rel="stylesheet" href="https://fonts.googleapis.com/css2?family=Montserrat:wght@300&family=Open+Sans:wght@400;600;700&display=swap">
<style>
  :root {
    --page-bg: #e9e7e5;
    --card-bg: #1d2024;
    --silver: #e4e4e4;
    --rose: #d9a39c;
    --text-light: #f2f2f2;
    --divider: #e6e6e6;
  }
  * { margin: 0; padding: 0; box-sizing: border-box; }
  html, body {
    width: 1200px; height: 864px; overflow: hidden;
    background: var(--page-bg);
    font-family: "Open Sans", Arial, sans-serif;
  }
  .sheet { position: relative; width: 1200px; height: 864px; }
  .card {
    position: absolute; top: 277px;
    width: 540px; height: 310px;
    background: var(--card-bg);
    border-radius: 4px;
    box-shadow: 0 10px 26px rgba(0,0,0,.25);
    overflow: hidden;
  }
  .card--front { left: 40px; }
  .card--back { left: 620px; }

  .wordmark {
    position: absolute;
    font-family: "Montserrat", Arial, sans-serif;
    font-weight: 300;
    line-height: 1;
    white-space: nowrap;
  }
  .card--front .wordmark {
    left: 92px; top: 108px;
    color: var(--silver);
    font-size: 36px; letter-spacing: 2px;
  }
  .card--back .wordmark {
    left: 34px; top: 142px;
    color: var(--rose);
    font-size: 27px; letter-spacing: 1px;
  }

  .front-url {
    position: absolute; left: 92px; top: 206px;
    color: var(--text-light);
    font-size: 15px; letter-spacing: 1.5px;
  }

  .divider {
    position: absolute; left: 262px; top: 70px;
    width: 2px; height: 170px;
    background: linear-gradient(to bottom, transparent, var(--divider) 25%, var(--divider) 75%, transparent);
  }

  .contact {
    position: absolute; left: 284px; top: 72px;
    color: var(--text-light);
  }
  .contact__name {
    color: var(--rose); font-weight: 700; font-size: 17px; letter-spacing: .5px;
  }
  .contact__title { font-size: 12px; letter-spacing: 1px; margin-bottom: 10px; }
  .contact__address { font-size: 13px; line-height: 1.35; margin-bottom: 8px; }
  .contact__list { list-style: none; font-size: 13px; }
  .contact__item { display: flex; align-items: center; gap: 7px; height: 20px; white-space: nowrap; }
  .contact__icon { width: 13px; height: 13px; flex: none; }
</style>
</head>
<body>
<main class="sheet">
  <section class="card card--front" aria-label="Business card front">
    <div class="wordmark">Corvel Music</div>
    <div class="front-url">www.corvelmusicevents.com</div>
  </section>

  <section class="card card--back" aria-label="Business card back">
    <div class="wordmark">Corvel Music</div>
    <div class="divider"></div>
    <div class="contact">
      <div class="contact__name">TESSA HOLLOWAY</div>
      <div class="contact__title">DIRECTOR | VIOLINIST</div>
      <div class="contact__address">Level 7, 41 Marlow Street<br>Sydney, 2000</div>
      <ul class="contact__list">
        <li class="contact__item">
          <svg class="contact__icon" viewBox="0 0 16 16" aria-hidden="true"><circle cx="8" cy="8" r="8" fill="var(--rose)"/><path d="M5 4.5h2l.6 2-1 .8a5 5 0 0 0 2.1 2.1l.8-1 2 .6v2c-4 .4-7-2.6-6.5-6.5z" fill="var(--card-bg)"/></svg>
          0481 352 604
        </li>
        <li class="contact__item">
          <svg class="contact__icon" viewBox="0 0 16 16" aria-hidden="true"><rect x="4" y="1" width="8" height="14" rx="1.5" fill="none" stroke="var(--rose)" stroke-width="1.5"/><circle cx="8" cy="12.3" r=".9" fill="var(--rose)"/></svg>
          0481 352 604
        </li>
        <li class="contact__item">
          <svg class="contact__icon" viewBox="0 0 16 16" aria-hidden="true"><rect x="1" y="3.5" width="14" height="9.5" fill="var(--rose)"/><path d="M1 3.5l7 5.5 7-5.5" fill="none" stroke="var(--card-bg)" stroke-width="1.2"/></svg>
          tessa@corvelmusicevents.com
        </li>
        <li class="contact__item">
          <svg class="contact__icon" viewBox="0 0 16 16" aria-hidden="true"><circle cx="8" cy="8" r="8" fill="var(--rose)"/><circle cx="8" cy="8" r="4.5" fill="none" stroke="var(--card-bg)" stroke-width="1.1"/><path d="M3.5 8h9M8 3.5v9" stroke="var(--card-bg)" stroke-width="1.1"/></svg>
          www.corvelmusicevents.com
        </li>
      </ul>
    </div>
  </section>
</main>
</body>
</html>
```